Personal Trainer and Corporate Health Business

I need a business card for a new company I'm starting in Australia called "Brisk Vigour Outreach" I will be providing a Personal training service as well as corporate health in companies.
The service provided is to help promote an active and healthy lifstyle.
The design should communicate a healthy lifestyle and also the benefits that this can have on a personal level and in the corporate environment and the benefits that flow from that.

Target Market(s)

Members of the public and Corporate

Industry/Entity Type

Environment

Requirements
Must have
• Company logo attached
Look and feel fresh and modern

Tag line: "Actively promoting a healthier lifestyle"

Colin Varga
Managing Director

m: 0412 657 394
e: colin@briskvigouroutreach.com.au

www.briskvigouroutreach.com.au
Nice to have
• Can be 1 or 2 sided

```html
<!DOCTYPE html>
<html lang="en">
<head>
<meta charset="utf-8">
<title>Brisk Vigour Outreach – Business Card</title>
<link href="https://fonts.googleapis.com/css2?family=Exo+2:wght@500;600;700&display=swap" rel="stylesheet">
<style>
  :root {
    --brand-blue: #0b5a9e;
    --brand-blue-deep: #064a86;
    --brand-green: #8dbb2f;
    --brand-green-light: #a3c93c;
    --card-white: #ffffff;
    --card-grey: #ececec;
    --stage: #e4e6e9;
    --contact-text: #f3f7e8;
  }
  * { box-sizing: border-box; margin: 0; padding: 0; }
  html, body {
    width: 1200px; height: 900px; overflow: hidden;
    background: var(--stage);
    font-family: "Exo 2", "Segoe UI", sans-serif;
  }
  .stage { position: relative; width: 1200px; height: 900px; }
  .card {
    position: absolute; left: 260px; width: 680px; height: 390px;
    border-radius: 22px; overflow: hidden;
    background: linear-gradient(135deg, var(--card-white) 40%, var(--card-grey));
    box-shadow: 0 10px 26px rgba(0,0,0,.18);
  }
  .card-front { top: 40px; }
  .card-back { top: 470px; }
  .card-art { position: absolute; inset: 0; width: 100%; height: 100%; }

  .brand-name {
    position: absolute; display: flex; align-items: center; gap: 10px;
    color: var(--brand-blue); font-weight: 600; letter-spacing: .02em;
    white-space: nowrap;
  }
  .brand-name .brand-dot {
    width: 14px; height: 14px; border-radius: 50%; background: var(--brand-blue);
    flex: none;
  }
  .card-front .brand-name { left: 46px; top: 172px; font-size: 26px; }
  .card-back .brand-name { right: 40px; top: 44px; font-size: 22px; }

  .holder { position: absolute; left: 70px; top: 128px; }
  .holder-name { color: var(--brand-blue); font-weight: 700; font-size: 27px; line-height: 1.1; }
  .holder-role { color: var(--brand-green); font-weight: 600; font-size: 17px; line-height: 1.3; }

  .contact-list {
    position: absolute; left: 392px; top: 258px; list-style: none;
    color: var(--contact-text); font-weight: 600; font-size: 15px; line-height: 1.55;
  }
  .contact-list .label { display: inline-block; width: 26px; }
</style>
</head>
<body>
<main class="stage">

  <section class="card card-front" aria-label="Business card front">
    <svg class="card-art" viewBox="0 0 680 390" aria-hidden="true">
      <path d="M480 0 C415 120 405 260 355 390 L680 390 L680 0 Z" fill="var(--brand-green)"/>
      <path d="M495 0 C435 120 423 260 375 390 L680 390 L680 0 Z" fill="var(--card-white)"/>
      <path d="M505 0 C445 120 435 260 387 390 L680 390 L680 0 Z" fill="var(--brand-blue)"/>
    </svg>
    <div class="brand-name"><span class="brand-dot"></span>Brisk Vigour Outreach</div>
  </section>

  <section class="card card-back" aria-label="Business card back">
    <svg class="card-art" viewBox="0 0 680 390" aria-hidden="true">
      <path d="M0 322 C200 272 440 192 680 172 L680 390 L0 390 Z" fill="var(--brand-green)"/>
      <path d="M0 300 C220 242 450 152 680 112 L680 136 C450 170 230 258 0 308 Z" fill="var(--brand-blue-deep)"/>
    </svg>
    <div class="brand-name"><span class="brand-dot"></span>Brisk Vigour Outreach</div>
    <div class="holder">
      <p class="holder-name">Colin Varga</p>
      <p class="holder-role">Managing Director</p>
    </div>
    <ul class="contact-list">
      <li><span class="label">m:</span>0412 657 394</li>
      <li><span class="label">e:</span>colin@briskvigouroutreach.com.au</li>
      <li><span class="label">w:</span>www.briskvigouroutreach.com.au</li>
    </ul>
  </section>

</main>
</body>
</html>
```